Mirelo Japanese Restaurant

We just want the japanese sakura background and the menu as below

Side dish :
Edamame $4
Japanese Steam Green Bean
Crab Craw $3 each
With Japanese mayo
Teriyaki Chicken stick $3 each
Chicken stick with home made teriyaki sauce
Tempura Prawns $7
With Japanese mayo
Miso Soup $3
Traditional Japanese soup
Salt and Pepper Calamari $7
With japanese mayo

Main dish:
Gyu Don $12
Bowl of steam rice topped with beef and onion simmered in a mildly sweet sauce.
Teriyaki Don $12
Bowl of steam rice topped with your choice of beef, chicken or pork and with our special Teriyaki sauce.
Vege Don $12
Bowl of steam rice with seasonal Vegetables with the special japanese sweet soy sauce.
Japanese Curry $12,(prawns $14)
Bowl of steam rice with Chicken, pork or prawn with japanese mild curry sauce.
Katsu Don $12
Bowl of steam rice topped with a deep-fried pork cutlet and egg with the japanese special sauce.
Oyako Don $12
Bowl of steam rice topped with chick and egg with japanese special sauce.
Spice Don $12
Bowl of steam rice topped with beef or chicken with japanese spice sauce.
Gingle Don $12
Bowl of steam rice topped with beef or chicken with japanese ginger sauce.
Sushi $3
Roll everyday on seasonal
ingredient.

Japanese-style sweets
Black Sesame Ice cream $4.5
Green tea Ice cream $4.5

```html
<!DOCTYPE html>
<html lang="en">
<head>
<meta charset="utf-8">
<title>Mirelo Japanese Restaurant – Menu</title>
<link rel="stylesheet" href="https://fonts.googleapis.com/css2?family=Lobster&family=Open+Sans:wght@400;700&display=swap">
<style>
  :root {
    --bg: #ece7e3;
    --paper: #ffffff;
    --pink: #ee5c7a;
    --pink-soft: #f5a3b5;
    --pink-band: #ef6380;
    --ink: #1d1d1d;
    --ink-soft: #333333;
  }
  * { margin: 0; padding: 0; box-sizing: border-box; }
  html, body { width: 1200px; height: 900px; overflow: hidden; background: var(--bg); }
  body { position: relative; font-family: "Open Sans", sans-serif; color: var(--ink); }

  .page { position: absolute; top: 48px; width: 541px; height: 773px; background: var(--paper); box-shadow: 0 4px 10px rgba(0,0,0,.25); overflow: hidden; }
  .page--left { left: 40px; }
  .page--right { left: 606px; width: 552px; }

  .top-band { position: absolute; left: 0; top: 0; width: 100%; height: 57px; background: var(--pink-band); }
  .bottom-band { position: absolute; left: 0; bottom: 0; width: 100%; height: 11px; background: var(--pink-band); z-index: 3; }

  .masthead { position: absolute; top: 0; left: 95px; width: 333px; height: 57px; background: linear-gradient(#fdf1f2, #f6dcdf); display: flex; align-items: center; z-index: 3; }
  .page--right .masthead { left: 104px; }
  .masthead__mark { width: 34px; height: 34px; border-radius: 50%; background: var(--pink); margin: 0 12px 0 18px; flex: none; }
  .masthead__name { font-weight: 700; font-size: 15px; line-height: 1.15; color: var(--ink-soft); width: 170px; }
  .masthead__art { position: absolute; right: 0; top: 0; width: 68px; height: 57px; background: linear-gradient(135deg, #f3ecec, #d9c9cb); border-left: 1px solid #fff; }

  .sakura { position: absolute; z-index: 0; background: radial-gradient(closest-side, rgba(247,214,222,.7), rgba(250,235,238,.45) 55%, rgba(255,255,255,0)); }

  .page-title { position: absolute; z-index: 2; left: 0; width: 100%; top: 115px; text-align: center; font-family: "Lobster", cursive; font-size: 46px; color: var(--ink); padding-left: 8px; }
  .section-title { position: absolute; z-index: 2; font-family: "Lobster", cursive; font-weight: 400; font-size: 20px; color: var(--pink); }

  .menu-list { position: absolute; z-index: 2; list-style: none; }
  .menu-item { position: absolute; left: 0; width: 100%; }
  .menu-item__name { font-weight: 700; font-size: 11px; line-height: 13px; }
  .menu-item__desc { font-size: 8px; line-height: 11px; color: var(--ink-soft); }
  .menu-item__price { position: absolute; top: 0; font-size: 11px; font-weight: 700; line-height: 13px; }
  .side-list .menu-item__price { left: 242px; }
  .main-list .menu-item__price, .sweets-list .menu-item__price { right: 0; text-align: right; }

  .photo-blob { position: absolute; z-index: 1; background: var(--pink-soft); border-radius: 20px 34px 18px 30px; opacity: .85; }
  .photo { position: absolute; z-index: 2; box-shadow: 0 2px 5px rgba(0,0,0,.35); }

  .blossom { position: absolute; z-index: 1; width: 100px; height: 90px; border-radius: 50%; background: radial-gradient(closest-side, #fdf6f7, #f2d6dc 60%, rgba(242,214,220,0)); }

  .tagline { position: absolute; z-index: 2; left: 127px; top: 678px; font-family: "Lobster", cursive; font-size: 18px; color: var(--pink); }
</style>
</head>
<body>

<section class="page page--left">
  <div class="top-band"></div>
  <header class="masthead">
    <span class="masthead__mark"></span>
    <span class="masthead__name">Mirelo<br>Japanese Restaurant</span>
    <div class="masthead__art" role="img" aria-label="Cherry blossom branch illustration"></div>
  </header>

  <div class="sakura" style="left:-40px;top:130px;width:400px;height:480px;" role="img" aria-label="Faded sakura tree background"></div>

  <h1 class="page-title">Menu</h1>
  <h2 class="section-title" style="left:56px;top:210px;">Side dish</h2>

  <ul class="menu-list side-list" style="left:55px;top:266px;width:300px;">
    <li class="menu-item" style="top:0;"><div class="menu-item__name">Edamame</div><div class="menu-item__desc">Japanese steam green bean</div><span class="menu-item__price">$4</span></li>
    <li class="menu-item" style="top:38px;"><div class="menu-item__name">Crab craw</div><div class="menu-item__desc">With Japanese mayo</div><span class="menu-item__price">$3 each</span></li>
    <li class="menu-item" style="top:75px;"><div class="menu-item__name">Teriyaki chicken stick</div><div class="menu-item__desc">Chicken stick with home made teriyaki sauce</div><span class="menu-item__price">$3 each</span></li>
    <li class="menu-item" style="top:113px;"><div class="menu-item__name">Tempura prawns</div><div class="menu-item__desc">With Japanese mayo</div><span class="menu-item__price" style="left:248px;">$7</span></li>
    <li class="menu-item" style="top:149px;"><div class="menu-item__name">Miso Soup</div><div class="menu-item__desc">Traditional Japanese soup</div><span class="menu-item__price" style="left:248px;">$3</span></li>
    <li class="menu-item" style="top:187px;"><div class="menu-item__name">Salt and Pepper Calamari</div><div class="menu-item__desc">With japanese mayo</div><span class="menu-item__price" style="left:248px;">$7</span></li>
  </ul>

  <div class="photo-blob" style="left:350px;top:231px;width:40px;height:40px;"></div>
  <div class="photo-blob" style="left:470px;top:283px;width:38px;height:42px;"></div>
  <div class="photo" style="left:367px;top:241px;width:114px;height:75px;background:linear-gradient(135deg,#c9a86a,#8f6b3c);" role="img" aria-label="Photo of fried crab claws on a plate"></div>
  <div class="photo-blob" style="left:352px;top:326px;width:40px;height:36px;"></div>
  <div class="photo-blob" style="left:470px;top:373px;width:37px;height:38px;"></div>
  <div class="photo" style="left:367px;top:335px;width:114px;height:72px;background:linear-gradient(135deg,#e58a5a,#d8b540);" role="img" aria-label="Photo of pickled ginger"></div>
  <div class="photo-blob" style="left:350px;top:424px;width:40px;height:36px;"></div>
  <div class="photo-blob" style="left:470px;top:476px;width:38px;height:40px;"></div>
  <div class="photo" style="left:367px;top:431px;width:114px;height:76px;background:linear-gradient(135deg,#2a1c14,#8a5a2a);" role="img" aria-label="Photo of miso soup bowl with spoon"></div>

  <div class="blossom" style="left:15px;top:650px;" role="img" aria-label="Cherry blossom flowers"></div>
  <div class="blossom" style="left:420px;top:650px;" role="img" aria-label="Cherry blossom flowers"></div>

  <p class="tagline">Roll everyday on seasonal ingredient.</p>
  <div class="bottom-band"></div>
</section>

<section class="page page--right">
  <div class="top-band"></div>
  <header class="masthead">
    <span class="masthead__mark"></span>
    <span class="masthead__name">Mirelo<br>Japanese Restaurant</span>
    <div class="masthead__art" role="img" aria-label="Cherry blossom branch illustration"></div>
  </header>

  <div class="sakura" style="left:150px;top:110px;width:440px;height:520px;" role="img" aria-label="Faded sakura tree background"></div>

  <div class="photo-blob" style="left:92px;top:114px;width:70px;height:40px;"></div>
  <div class="photo-blob" style="left:140px;top:340px;width:28px;height:46px;"></div>
  <div class="photo" style="left:50px;top:132px;width:109px;height:250px;background:linear-gradient(160deg,#f2f2f2,#d9a255 55%,#c8283a);" role="img" aria-label="Photo of a rice bowl with chopsticks and soy sauce"></div>
  <div class="photo-blob" style="left:40px;top:560px;width:40px;height:108px;"></div>
  <div class="photo" style="left:50px;top:402px;width:109px;height:210px;background:linear-gradient(170deg,#3a3631,#5b4d3e 45%,#e19a3c 60%,#7a8a52);" role="img" aria-label="Photo of Japanese sweets with orange slice"></div>

  <h2 class="section-title" style="left:203px;top:110px;">Main dish</h2>

  <ul class="menu-list main-list" style="left:194px;top:162px;width:272px;">
    <li class="menu-item" style="top:0;"><div class="menu-item__name">Gyu Don</div><div class="menu-item__desc">Bowl of steam rice topped with beef and onion<br>simmered in a mildly sweet sauce.</div><span class="menu-item__price" style="right:8px;">$12</span></li>
    <li class="menu-item" style="top:46px;"><div class="menu-item__name">Teriyaki Don</div><div class="menu-item__desc">Bowl of steam rice topped with your choice of beef, chicken or<br>pork and with our special Teriyaki sauce.</div><span class="menu-item__price" style="right:8px;">$12</span></li>
    <li class="menu-item" style="top:93px;"><div class="menu-item__name">Vege Don</div><div class="menu-item__desc">Bowl of steam rice with seasonal Vegetables with the special<br>japanese sweet soy sauce.</div><span class="menu-item__price" style="right:8px;">$12</span></li>
    <li class="menu-item" style="top:139px;"><div class="menu-item__name">Japanese Curry</div><div class="menu-item__desc" style="margin-top:12px;">Bowl of steam rice with Chicken, pork or prawn<br>with japanese mild curry sauce.</div><span class="menu-item__price">$12,<br>(prawns $14)</span></li>
    <li class="menu-item" style="top:201px;"><div class="menu-item__name">Katsu Don</div><div class="menu-item__desc">Bowl of steam rice topped with a deep-fried pork cutlet and egg<br>with the japanese special sauce.</div><span class="menu-item__price">$12</span></li>
    <li class="menu-item" style="top:248px;"><div class="menu-item__name">Oyako Don</div><div class="menu-item__desc">Bowl of steam rice topped with chick and egg with japanese<br>special sauce.</div><span class="menu-item__price">$12</span></li>
    <li class="menu-item" style="top:283px;"><div class="menu-item__name">Spice Don</div><div class="menu-item__desc">Bowl of steam rice topped with beef or chicken<br>with japanese spice sauce.</div><span class="menu-item__price">$12</span></li>
    <li class="menu-item" style="top:332px;"><div class="menu-item__name">Gingle Don</div><div class="menu-item__desc">Bowl of steam rice topped with beef or chicken<br>with japanese ginger sauce.</div><span class="menu-item__price">$12</span></li>
    <li class="menu-item" style="top:381px;"><div class="menu-item__name">Sushi</div><span class="menu-item__price">$3</span></li>
  </ul>

  <h2 class="section-title" style="left:194px;top:590px;">Japanese-style sweets</h2>
  <ul class="menu-list sweets-list" style="left:194px;top:637px;width:260px;">
    <li class="menu-item" style="top:0;"><div class="menu-item__name">Black Sesame Ice cream</div><span class="menu-item__price">$4.5</span></li>
    <li class="menu-item" style="top:27px;"><div class="menu-item__name">&nbsp;Green tea Ice cream</div><span class="menu-item__price">$4.5</span></li>
  </ul>

  <div class="blossom" style="left:22px;top:655px;" role="img" aria-label="Cherry blossom flowers"></div>
  <div class="blossom" style="left:432px;top:655px;" role="img" aria-label="Cherry blossom flowers"></div>

  <div class="bottom-band"></div>
</section>

</body>
</html>
```